Web Page Color Scheme

I need the colors chosen for all of the elements in a B2B web application page (screenshot attached).

We have a web application that serves businesses (not consumers), generally Corvane 300 companies. The pages are fully developed/functional. What I want is to improve the look and feel so that the page has a more premium feel. That is the entire goal, to make the pages have a very premium feel to them. I don’t know if it is the best analogy but if you think of Varn or Pallisene as average and KTR or Osprin as premium, we want users to get a very premium feel the first time they see the screens.

What I am looking for right now is just colors. Below I describe the details.

#1 Improve the colors

The color scheme is blue and yellow. Black, gray and white are also used. I do not think the base colors should change (that is, I think we will continue to use blue and yellow) but I do think which hues, shades, tints or tones of blue, yellow and gray we use could benefit from some improvement. Feel free to use any blues, yellows and grays you think look best, lighter or darker colors, etc. You can also feel free to change what colors are used where. One note, aqua blue does not look premium. It might be deco looking or otherwise good for some things but I don’t think you will see an aqua colored Hollaway driving down the street any time soon.

Quill products tend to have a premium feel but I don’t think I am looking for a stark white appearance.

I want every color defined including but not necessarily limited to:

Backgrounds

Page Header
Navigation Panel
Page Body
Table Header
Table Header Button (the Add button)
Table Column Header
Table Rows (maybe alternating, maybe not)
Checkboxes
Table Footer

Not all of these have to be different. I assume some will be the same. I just need each carefully
thought through.

Fonts

Page Header
Navigation Panel
Page Title
Table Header Title
Table Header Button
Table Column Header
Table Row
Table Footer

Icons

Page Header
Navigation Panel
Table expander/collapse
Actions
Table Footer

Target Market(s)

Corvane 300/Pinnacle 1200

Requirements
Must have
• Premium feel

```html
<!DOCTYPE html>
<html lang="en">
<head>
<meta charset="utf-8">
<title>Data Source</title>
<link rel="stylesheet" href="https://fonts.googleapis.com/css2?family=Fira+Sans:ital,wght@0,400;0,500;0,600;1,400&display=swap">
<style>
:root{
  --header-bg:#050a19;
  --nav-bg:#e9e9e9;
  --nav-band:#dcdcdc;
  --body-bg:#f2f2f2;
  --navy:#0a1a3f;
  --blue:#1f5fa8;
  --yellow:#f5c400;
  --colhead:#e3e3e3;
  --line:#d6d6d6;
  --ink:#111;
  --muted:#6b6b6b;
  --rt-purple:#7b16a8;
  --rt-orange:#d2550a;
  --rt-red:#cf1f12;
  --rt-magenta:#b0109a;
  --rt-teal:#0f8fb3;
  --rt-green:#1a9a3c;
}
*{box-sizing:border-box;margin:0;padding:0}
html,body{width:1194px;height:1200px;overflow:hidden}
body{font-family:"Fira Sans",sans-serif;background:var(--body-bg);color:var(--ink);position:relative;font-size:12px}
.icon{width:13px;height:13px;fill:currentColor;display:block}

.topbar{position:absolute;left:0;top:0;width:1194px;height:63px;background:var(--header-bg);color:#fff;display:flex;align-items:center}
.brand{margin-left:22px;font-size:20px;font-weight:400;letter-spacing:.3px}
.menu-btn{margin-left:20px;width:17px;height:12px;border-top:2px solid #fff;border-bottom:2px solid #fff;position:relative}
.menu-btn::after{content:"";position:absolute;left:0;right:0;top:3px;border-top:2px solid #fff}
.top-tools{margin-left:auto;display:flex;align-items:center;gap:13px;margin-right:20px}
.top-tools svg{width:17px;height:17px;stroke:#fff;fill:none;stroke-width:1.4}
.user{margin-left:24px;font-weight:500;font-size:12.5px;display:flex;align-items:center;gap:5px}

.nav{position:absolute;left:0;top:63px;width:210px;height:1137px;background:var(--nav-bg)}
.nav-item{height:42px;background:var(--nav-band);display:flex;align-items:center;padding-left:18px;gap:10px;font-size:11px;font-weight:500;text-transform:uppercase;color:var(--navy)}
.nav-item svg{width:16px;height:16px;fill:var(--navy)}
.nav-item.active{color:var(--blue);border-left:4px solid var(--blue);padding-left:14px}
.nav-item.active svg{fill:var(--blue)}
.nav-sub{position:relative;padding:10px 0 14px 42px;font-size:11px;font-weight:500;color:var(--navy);line-height:18.5px}
.nav-sub::before{content:"";position:absolute;left:28px;top:4px;bottom:22px;border-left:1px solid #555}
.nav-sub li{list-style:none;position:relative}
.nav-sub li::before{content:"";position:absolute;left:-14px;top:9px;width:8px;border-top:1px solid #555}
.gap{height:12px}

.page-title{position:absolute;left:245px;top:112px;font-size:22px;font-weight:400;color:var(--navy)}
.search{position:absolute;left:949px;top:105px;width:210px;height:28px;background:#fff;border-radius:14px}
.search svg{position:absolute;right:10px;top:7px;width:13px;height:13px;stroke:#bbb;fill:none;stroke-width:1.6}

.grid{position:absolute;left:245px;top:143px;width:914px}
.bar{height:28px;background:var(--navy);color:#fff;display:flex;align-items:center;justify-content:space-between;padding:0 10px;font-size:11px;font-weight:600;text-transform:uppercase}
.add{color:var(--yellow);font-weight:500;font-size:11.5px}
.row{display:grid;align-items:center;height:36.7px;border-bottom:1px solid var(--line);font-size:12px}
.row>div{height:100%;display:flex;align-items:center;border-left:1px solid var(--line);padding-left:10px;white-space:nowrap;overflow:hidden}
.row>div:first-child{border-left:none}
.colhead{height:24.5px;background:var(--colhead);font-size:9.5px;text-transform:uppercase;color:var(--muted);border-bottom:none}
.colhead>div{border-left-color:#fff}
.main{grid-template-columns:318px 359px 144px 93px}
.objs{grid-template-columns:790px 93px}
.fields{grid-template-columns:255px 280px 79px 144px 93px}
.nest1{margin-left:31px}
.nest2{margin-left:32px}
.c{justify-content:center;padding-left:0 !important}
.exp{width:14px;height:14px;margin-right:9px;flex:none}
.sort{margin-left:6px;width:7px;height:10px;fill:#777}
.acts{gap:10px;justify-content:center;padding-left:0 !important}
.fields .name,.fields .type{padding-left:12px}
.cnt{font-style:italic;font-size:10px;margin-left:3px}

.chk{width:13px;height:13px;border-radius:3px;background:#e2e2e2;border:1px solid #e2e2e2}
.chk.on{background:#fff;border:1px solid var(--blue);position:relative}
.chk.on::after{content:"";position:absolute;left:3px;top:1px;width:4px;height:7px;border:solid var(--blue);border-width:0 1.5px 1.5px 0;transform:rotate(45deg)}

.rules{gap:4px;justify-content:center;padding-left:0 !important}
.rt{width:17px;height:17px;border:1px solid #999;background:#f6f6f6;position:relative}
.rt::after{content:"";position:absolute;left:4px;top:4px;width:7px;height:7px;border:1.5px solid #888;border-radius:2px}
.rt.p{background:var(--rt-purple);border-color:var(--rt-purple)}
.rt.o{background:var(--rt-orange);border-color:var(--rt-orange)}
.rt.r{background:var(--rt-red);border-color:var(--rt-red)}
.rt.m{background:var(--rt-magenta);border-color:var(--rt-magenta)}
.rt.t{background:var(--rt-teal);border-color:var(--rt-teal)}
.rt.g{background:var(--rt-green);border-color:var(--rt-green)}
.rt.p::after,.rt.o::after,.rt.r::after,.rt.m::after,.rt.t::after,.rt.g::after{border-color:#fff}
.rt.t::after{border-radius:50%}

.pager{position:absolute;left:574px;top:1103px;width:256px;text-align:center}
.records{font-size:8.5px;color:var(--muted);text-transform:uppercase;padding-bottom:5px;border-bottom:1px solid #bbb}
.pages{display:flex;justify-content:center;align-items:center;gap:12px;height:22px;color:#777;font-size:12px;border-bottom:1px solid #c8cde0}
.pages .cur{width:18px;height:18px;border-radius:50%;background:#ddd;line-height:18px;font-size:10px}
.result{position:absolute;left:1035px;top:1127px;display:flex;align-items:center;gap:6px;font-size:9px;color:var(--muted)}
.result span.sel{width:53px;height:20px;background:#fff;display:flex;align-items:center;padding-left:10px;font-size:9.5px;color:#555}
</style>
</head>
<body>
<svg width="0" height="0" style="position:absolute">
  <symbol id="i-bolt" viewBox="0 0 16 16"><path d="M10 1 3 9h4l-2 6 8-9H9l2-5z"/></symbol>
  <symbol id="i-edit" viewBox="0 0 16 16"><path d="M3 11l7-7 2 2-7 7H3z"/><rect x="2" y="14" width="12" height="1.4"/></symbol>
  <symbol id="i-file" viewBox="0 0 16 16"><path d="M3 1h6l4 4v10H3z"/></symbol>
  <symbol id="i-trash" viewBox="0 0 16 16"><rect x="2" y="2" width="12" height="2"/><rect x="6" y="0.5" width="4" height="2"/><path d="M3.5 5h9l-1 10h-7zM6 7v6h1.2V7zm2.8 0v6H10V7z" fill-rule="evenodd"/></symbol>
  <symbol id="i-right" viewBox="0 0 16 16"><circle cx="8" cy="8" r="8" fill="#1f5fa8"/><path d="M6.5 4.5 10 8l-3.5 3.5" stroke="#fff" stroke-width="2" fill="none"/></symbol>
  <symbol id="i-down" viewBox="0 0 16 16"><circle cx="8" cy="8" r="8" fill="#1f5fa8"/><path d="M4.5 6.5 8 10l3.5-3.5" stroke="#fff" stroke-width="2" fill="none"/></symbol>
  <symbol id="i-sort" viewBox="0 0 8 12"><path d="M4 0 8 5H0zM4 12 0 7h8z"/></symbol>
</svg>

<header class="topbar">
  <div class="brand">Orvella Data</div>
  <div class="menu-btn"></div>
  <div class="top-tools">
    <svg viewBox="0 0 16 16"><rect x="1" y="1" width="5" height="6"/><rect x="9" y="1" width="6" height="4"/><rect x="1" y="10" width="5" height="5"/><rect x="9" y="8" width="6" height="7"/></svg>
    <svg viewBox="0 0 16 16"><path d="M2 14 11 5M10 2v2M13 5h2M12 3l1.5-1.5"/></svg>
    <svg viewBox="0 0 16 16"><circle cx="8" cy="8" r="7"/><path d="M6 6a2 2 0 1 1 2.5 2c-.5.2-.5.8-.5 1.5M8 11.5v1"/></svg>
    <svg viewBox="0 0 16 16"><circle cx="8" cy="8" r="2.5"/><circle cx="8" cy="8" r="6" stroke-dasharray="2.5 1.6"/></svg>
    <div class="user">Tobin Ashlake <svg viewBox="0 0 10 10" style="width:10px;height:10px"><path d="M1 3l4 4 4-4"/></svg></div>
  </div>
</header>

<nav class="nav">
  <div class="nav-item"><svg viewBox="0 0 16 16"><circle cx="5.5" cy="5" r="3"/><path d="M0 14c0-4 2.5-5 5.5-5s5.5 1 5.5 5z"/><circle cx="11" cy="4.5" r="2.5"/><path d="M12 8.5c2.5.3 4 1.5 4 5h-4z"/></svg>Users</div>
  <ul class="nav-sub"><li>Roles</li><li>Notification Groups</li></ul>
  <div class="gap"></div>
  <div class="nav-item active"><svg viewBox="0 0 16 16"><ellipse cx="8" cy="3" rx="6.5" ry="2.2"/><path d="M1.5 5c0 3 13 3 13 0v3c0 3-13 3-13 0zM1.5 10c0 3 13 3 13 0v3c0 3-13 3-13 0z"/></svg>Data Sources</div>
  <ul class="nav-sub"><li>Data Object Relationships</li></ul>
  <div class="gap"></div>
  <div class="nav-item"><svg viewBox="0 0 16 16"><path d="M1 1h6v6H1zm2 2v2h2V3zM9 1h6v6H9zm2 2v2h2V3zM1 9h6v6H1zm2 2v2h2v-2zM9 9h6v6H9zm2 2v2h2v-2z" fill-rule="evenodd"/></svg>Data Sets</div>
  <div class="nav-item"><svg viewBox="0 0 16 16"><rect x="0" y="1" width="3" height="2"/><rect x="5" y="1" width="11" height="2"/><rect x="2" y="5" width="3" height="2"/><rect x="7" y="5" width="9" height="2"/><rect x="2" y="9" width="3" height="2"/><rect x="7" y="9" width="9" height="2"/><rect x="2" y="13" width="3" height="2"/><rect x="7" y="13" width="9" height="2"/></svg>Rule Sets</div>
  <div class="nav-item"><svg viewBox="0 0 16 16"><path d="M8 0a8 8 0 1 1 0 16A8 8 0 0 1 8 0zm0 2a6 6 0 1 0 0 12A6 6 0 0 0 8 2zm-1 2h2v4.5l3 2-1 1.5-4-2.7z" fill-rule="evenodd"/></svg>Schedules</div>
  <div class="nav-item"><svg viewBox="0 0 16 16"><path d="M3 0l3 3H4v8h8v2H2V3H0zM13 16l-3-3h2V5H4V3h10v10h2z"/></svg>Metadata Import/Export</div>
  <ul class="nav-sub"><li>Import</li><li>Export</li></ul>
</nav>

<h1 class="page-title">DATA SOURCE</h1>
<div class="search"><svg viewBox="0 0 14 14"><circle cx="6" cy="6" r="4.5"/><path d="M9.5 9.5 13 13"/></svg></div>

<section class="grid">
  <div class="bar"><span>Data Source</span><span class="add">+ ADD</span></div>
  <div class="row main colhead">
    <div style="padding-left:31px">Data Source Name<svg class="sort"><use href="#i-sort"/></svg></div>
    <div>Type<svg class="sort"><use href="#i-sort"/></svg></div>
    <div class="c">Status<svg class="sort"><use href="#i-sort"/></svg></div>
    <div class="c">Action</div>
  </div>

  <div class="row main"><div><svg class="exp"><use href="#i-right"/></svg>relbase</div><div>Nimbrel.net</div><div class="c">Active</div><div class="acts"><svg class="icon"><use href="#i-bolt"/></svg><svg class="icon"><use href="#i-edit"/></svg><svg class="icon"><use href="#i-file"/></svg><svg class="icon"><use href="#i-trash"/></svg></div></div>
  <div class="row main"><div><svg class="exp"><use href="#i-right"/></svg>Nimbrel - Sandbox</div><div>Nimbrel.net</div><div class="c">Active</div><div class="acts"><svg class="icon"><use href="#i-bolt"/></svg><svg class="icon"><use href="#i-edit"/></svg><svg class="icon"><use href="#i-file"/></svg><svg class="icon"><use href="#i-trash"/></svg></div></div>
  <div class="row main"><div><svg class="exp"><use href="#i-right"/></svg>NMBL</div><div>Nimbrel.net</div><div class="c">Active</div><div class="acts"><svg class="icon"><use href="#i-bolt"/></svg><svg class="icon"><use href="#i-edit"/></svg><svg class="icon"><use href="#i-file"/></svg><svg class="icon"><use href="#i-trash"/></svg></div></div>
  <div class="row main"><div><svg class="exp"><use href="#i-down"/></svg>nmbl 44</div><div>Nimbrel.net</div><div class="c">Active</div><div class="acts"><svg class="icon"><use href="#i-bolt"/></svg><svg class="icon"><use href="#i-edit"/></svg><svg class="icon"><use href="#i-file"/></svg><svg class="icon"><use href="#i-trash"/></svg></div></div>

  <div class="nest1">
    <div class="bar"><span>Data Objects</span><span class="add">+ ADD</span></div>
    <div class="row objs colhead"><div style="padding-left:31px">Data Object Name</div><div class="c">Action</div></div>
    <div class="row objs"><div><svg class="exp"><use href="#i-down"/></svg>Account<span class="cnt">(28 fields)</span></div><div class="c"><svg class="icon"><use href="#i-trash"/></svg></div></div>

    <div class="nest2">
      <div class="bar"><span>Fields</span><span class="add">+ ADD</span></div>
      <div class="row fields colhead"><div>Field Name</div><div>Data Type</div><div class="c">Primary Key</div><div class="c">Rule Types</div><div class="c">Action</div></div>

      <div class="row fields"><div class="name">Id</div><div class="type">Common.ID</div><div class="c"><span class="chk on"></span></div><div class="rules"><i class="rt"></i><i class="rt"></i><i class="rt"></i><i class="rt"></i><i class="rt"></i><i class="rt"></i></div><div class="acts"><svg class="icon"><use href="#i-edit"/></svg><svg class="icon"><use href="#i-trash"/></svg></div></div>
      <div class="row fields"><div class="name">Name</div><div class="type">Organization.Name</div><div class="c"><span class="chk"></span></div><div class="rules"><i class="rt p"></i><i class="rt o"></i><i class="rt r"></i><i class="rt m"></i><i class="rt t"></i><i class="rt g"></i></div><div class="acts"><svg class="icon"><use href="#i-edit"/></svg><svg class="icon"><use href="#i-trash"/></svg></div></div>
      <div class="row fields"><div class="name">Phone</div><div class="type">Phone.Phone Number</div><div class="c"><span class="chk"></span></div><div class="rules"><i class="rt p"></i><i class="rt o"></i><i class="rt r"></i><i class="rt m"></i><i class="rt t"></i><i class="rt g"></i></div><div class="acts"><svg class="icon"><use href="#i-edit"/></svg><svg class="icon"><use href="#i-trash"/></svg></div></div>
      <div class="row fields"><div class="name">BillingCity</div><div class="type">Address.City</div><div class="c"><span class="chk"></span></div><div class="rules"><i class="rt p"></i><i class="rt o"></i><i class="rt r"></i><i class="rt m"></i><i class="rt t"></i><i class="rt g"></i></div><div class="acts"><svg class="icon"><use href="#i-edit"/></svg><svg class="icon"><use href="#i-trash"/></svg></div></div>
      <div class="row fields"><div class="name">BillingCountry</div><div class="type">Address.Country</div><div class="c"><span class="chk"></span></div><div class="rules"><i class="rt p"></i><i class="rt o"></i><i class="rt r"></i><i class="rt m"></i><i class="rt t"></i><i class="rt g"></i></div><div class="acts"><svg class="icon"><use href="#i-edit"/></svg><svg class="icon"><use href="#i-trash"/></svg></div></div>
      <div class="row fields"><div class="name">BillingLatitude</div><div class="type">Geographic.Latitude</div><div class="c"><span class="chk"></span></div><div class="rules"><i class="rt p"></i><i class="rt"></i><i class="rt r"></i><i class="rt"></i><i class="rt t"></i><i class="rt g"></i></div><div class="acts"><svg class="icon"><use href="#i-edit"/></svg><svg class="icon"><use href="#i-trash"/></svg></div></div>
      <div class="row fields"><div class="name">BillingLongitude</div><div class="type">Geographic.Longitude</div><div class="c"><span class="chk"></span></div><div class="rules"><i class="rt p"></i><i class="rt"></i><i class="rt r"></i><i class="rt"></i><i class="rt t"></i><i class="rt g"></i></div><div class="acts"><svg class="icon"><use href="#i-edit"/></svg><svg class="icon"><use href="#i-trash"/></svg></div></div>
      <div class="row fields"><div class="name">BillingState</div><div class="type">Address.State or Providence</div><div class="c"><span class="chk"></span></div><div class="rules"><i class="rt p"></i><i class="rt"></i><i class="rt r"></i><i class="rt"></i><i class="rt t"></i><i class="rt g"></i></div><div class="acts"><svg class="icon"><use href="#i-edit"/></svg><svg class="icon"><use href="#i-trash"/></svg></div></div>
      <div class="row fields"><div class="name">BillingStreet</div><div class="type">Address.Adress Line 1</div><div class="c"><span class="chk"></span></div><div class="rules"><i class="rt p"></i><i class="rt"></i><i class="rt r"></i><i class="rt"></i><i class="rt t"></i><i class="rt g"></i></div><div class="acts"><svg class="icon"><use href="#i-edit"/></svg><svg class="icon"><use href="#i-trash"/></svg></div></div>
      <div class="row fields"><div class="name">BillingPostalCode</div><div class="type">Address.Zip or Postal Code</div><div class="c"><span class="chk"></span></div><div class="rules"><i class="rt p"></i><i class="rt"></i><i class="rt r"></i><i class="rt"></i><i class="rt t"></i><i class="rt g"></i></div><div class="acts"><svg class="icon"><use href="#i-edit"/></svg><svg class="icon"><use href="#i-trash"/></svg></div></div>
      <div class="row fields"><div class="name">LastModifiedDate</div><div class="type">Common.Last Updated Date</div><div class="c"><span class="chk"></span></div><div class="rules"><i class="rt"></i><i class="rt"></i><i class="rt"></i><i class="rt"></i><i class="rt t"></i><i class="rt g"></i></div><div class="acts"><svg class="icon"><use href="#i-edit"/></svg><svg class="icon"><use href="#i-trash"/></svg></div></div>
      <div class="row fields"><div class="name">Website</div><div class="type">Organization.Wbsite/URL</div><div class="c"><span class="chk"></span></div><div class="rules"><i class="rt p"></i><i class="rt"></i><i class="rt r"></i><i class="rt"></i><i class="rt t"></i><i class="rt g"></i></div><div class="acts"><svg class="icon"><use href="#i-edit"/></svg><svg class="icon"><use href="#i-trash"/></svg></div></div>
    </div>

    <div class="row objs"><div><svg class="exp"><use href="#i-right"/></svg>Contact<span class="cnt">(26 fields)</span></div><div class="c"><svg class="icon"><use href="#i-trash"/></svg></div></div>
    <div class="row objs"><div><svg class="exp"><use href="#i-right"/></svg>Lead<span class="cnt">(17 fields)</span></div><div class="c"><svg class="icon"><use href="#i-trash"/></svg></div></div>
  </div>

  <div class="row main"><div><svg class="exp"><use href="#i-right"/></svg>nmbl 99</div><div>Nimbrel.net</div><div class="c">Active</div><div class="acts"><svg class="icon"><use href="#i-bolt"/></svg><svg class="icon"><use href="#i-edit"/></svg><svg class="icon"><use href="#i-file"/></svg><svg class="icon"><use href="#i-trash"/></svg></div></div>
  <div class="row main"><div><svg class="exp"><use href="#i-right"/></svg>NMBL - Field Entry Test</div><div>Nimbrel.net</div><div class="c">Active</div><div class="acts"><svg class="icon"><use href="#i-bolt"/></svg><svg class="icon"><use href="#i-edit"/></svg><svg class="icon"><use href="#i-file"/></svg><svg class="icon"><use href="#i-trash"/></svg></div></div>
</section>

<div class="pager">
  <div class="records">6 of 6 records</div>
  <div class="pages"><span>«</span><span>‹</span><span class="cur">1</span><span>›</span><span>»</span></div>
</div>
<div class="result">Result Displayed: <span class="sel">20</span></div>
</body>
</html>
```